Kaffeerösterei sucht Etiketten-Design
- schnelle Ausführung - mein Geschmack voll getroffen - unkompliziert und Kunden orientiert bei der Ausführung
Zielgruppe
Kaffeerösterei für die edelsten und teuersten Rohkaffees.
Meine Kunden sind Kaffee Geniesser.
Aufgabenstellung
Transparente Aufkleber für eine Schiefertafel im Format 22.5 cm x 15.5 cm.
Im Hand-Lettering Stil.
5 Schiefertafeln sind gewünscht.
Tafel 1
Kostenlos zur Degustation
Espresso
Café Crème 3.--
Americano 3.--
Filter Kaffee 3.--
Tafel 2
Kaffee & Milch
Cappuccino 4.--
Café Latte 4.--
Flat White 4.--
Latte Macchiato 4.--
Latte Macchiato mit Aroma 5.--
Kaffee & Hafermilch + 1.--
Tafel 3
Crepes
Pikant
- Pizza Crepes 7.--
- Flammkuchen Crepes 7.--
Süss
- Schoggi Crepes 6.--
- Apfelmus & Zimtzucker 6.--
Tafel 4
Kaffee & Schnaps
- Original Entlebucher Schwarzes 7.--
- Espresso Coretto 5.00
- Schwarzes mit Rahmhaube 8.--
Tafel 5
Schokolade & Milch
- heisse Schoggi 5.--
- heisse Schoggi mit Rahmhaube 6.--
- heisse Schoggi mit Espresso 6.--
- Schokolade & Hafermilch +1.--
Als Idee, was mir gefallen könnte:
https://www.bildsammlung.example/pin/104857392018374655/
https://de.grafikhort.example/vektorkunst/4418203-set-kaffeekarte-mit-tassen-kaffeegetranken-im-vintage-stil-stilisierte-zeichnung-mit-kreide-auf-tafel-schriftzug-sample-drinks
https://www.fotolager.example/stockfoto-heisser-kakao-bar-warm-hier-oben-hand-tafel-caf-schild-an-tafel-hintergrund-mit-farbe-kreide-schriftzug-werbung-fur-heisse-d-583021746.html

```html
<!DOCTYPE html>
<html lang="de">
<head>
<meta charset="utf-8">
<title>Crepes – Tafel</title>
<link rel="stylesheet" href="https://fonts.googleapis.com/css2?family=Amatic+SC:wght@700&display=swap">
<style>
  :root {
    --paper: #ffffff;
    --board: #1d1d1b;
    --chalk: #ffffff;
    --gold: #ffcf70;
    --cream: #fde9cf;
    --art-light: #6b6b66;
    --art-mid: #4a4a46;
    --art-dark: #2e2e2b;
  }
  * { margin: 0; padding: 0; box-sizing: border-box; }
  html, body {
    width: 1200px; height: 879px; overflow: hidden;
    background: var(--paper);
  }
  .sign {
    position: relative; width: 1200px; height: 879px;
    font-family: "Amatic SC", "Arial Narrow", sans-serif;
    font-weight: 700;
    color: var(--chalk);
  }
  .board {
    position: absolute; left: 61px; top: 61px;
    width: 1073px; height: 742px;
    background: var(--board);
  }
  .chalk-lines { position: absolute; left: 0; top: 0; }
  .title {
    position: absolute; left: 245px; top: 122px; width: 320px;
    text-align: center; font-size: 132px; line-height: 1; letter-spacing: 7px;
    font-weight: 700;
  }
  .star {
    position: absolute; top: 176px; font-size: 60px; line-height: 1;
  }
  .star--left { left: 214px; }
  .star--right { left: 560px; }
  .crepe-art {
    position: absolute; left: 700px; top: 117px;
    width: 372px; height: 322px;
    background:
      linear-gradient(180deg, var(--art-light) 0%, var(--art-mid) 45%, var(--art-dark) 100%);
    border-radius: 28px 28px 40px 40px;
  }
  .section-title {
    position: absolute; top: 408px;
    font-size: 84px; line-height: 1; color: var(--gold); letter-spacing: 5px;
    font-weight: 700;
  }
  .section-title--savoury { left: 166px; }
  .section-title--sweet { left: 606px; }
  .item {
    position: absolute; font-size: 62px; line-height: 1; letter-spacing: 5px;
  }
  .price {
    position: absolute; font-size: 62px; line-height: 1; letter-spacing: 4px;
    color: var(--cream);
  }
</style>
</head>
<body>
<main class="sign">
  <div class="board"></div>

  <svg class="chalk-lines" width="1200" height="879" viewBox="0 0 1200 879" aria-hidden="true">
    <g fill="none" stroke="var(--chalk)" stroke-width="3.5" stroke-linecap="round">
      <path d="M86 91 L396 83"/>
      <path d="M410 83 L420 83 M432 83 L438 83 M456 84 L464 85"/>
      <path d="M770 88 L776 88 M786 88 L804 88 M815 87 L1098 94"/>
      <path d="M84 88 Q80 430 88 768"/>
      <path d="M88 770 L1102 762"/>
      <path d="M1104 97 Q1100 420 1104 764"/>
      <path d="M1040 745 L1078 748 M1080 710 L1082 736"/>
      <circle cx="89" cy="92" r="6"/>
      <circle cx="1098" cy="98" r="6"/>
      <circle cx="92" cy="768" r="6"/>
      <circle cx="1100" cy="759" r="6"/>
    </g>
    <g fill="var(--chalk)">
      <circle cx="1082" cy="690" r="2.5"/>
      <circle cx="1028" cy="745" r="2.5"/>
    </g>
    <g fill="none" stroke="var(--gold)" stroke-linecap="round" stroke-width="6">
      <path d="M150 171 Q175 176 192 187"/>
      <path d="M126 196 L182 202"/>
      <path d="M150 228 Q170 218 188 212"/>
      <path d="M606 191 Q630 184 650 184"/>
      <path d="M614 209 L670 213"/>
      <path d="M608 218 Q628 228 640 240"/>
      <path d="M176 272 Q400 262 652 276" stroke-width="9"/>
    </g>
  </svg>

  <span class="star star--left" aria-hidden="true">*</span>
  <h1 class="title">Crepes</h1>
  <span class="star star--right" aria-hidden="true">*</span>

  <div class="crepe-art" role="img" aria-label="Kreidezeichnung: Stapel gefalteter Crepes mit Beeren, Erdbeere und Minzblättern"></div>

  <h2 class="section-title section-title--savoury">Pikant</h2>
  <h2 class="section-title section-title--sweet">Süss</h2>

  <p class="item" style="left:168px; top:503px;">Pizza Crepes</p>
  <p class="price" style="left:456px; top:503px;">7,–</p>
  <p class="item" style="left:168px; top:578px;">Flammkuchen</p>
  <p class="item" style="left:166px; top:647px;">Crepes</p>
  <p class="price" style="left:456px; top:647px;">7,–</p>

  <p class="item" style="left:607px; top:503px;">Schoggi Crepes</p>
  <p class="price" style="left:950px; top:503px;">6,–</p>
  <p class="item" style="left:607px; top:578px;">Apfelmus &amp;</p>
  <p class="item" style="left:607px; top:647px;">Zimtzucker</p>
  <p class="price" style="left:950px; top:647px;">6,–</p>
</main>
</body>
</html>
```